Business software developers new website

We need to redesign our website. Our current website is http://www.quorvanta.net/index.html, which is outdated and needs a new look. We moved out from web design and have concentrated more on the back end of the systems, for example, system support and security and cloud-based applications. Our major clients include both private and government sectors. We would like to see some designs that are all in one page, simple and clean. Prefer illustrator or obstructed images instead of real-life photos. Must look futuristic yet friendly. Attached the new logo for your references and good luck.

Target Market(s)

Medium to big company for their IT or data management. Either improve or upgrade their current system.

Industry/Entity Type

Business Software

Number of Pages Required

1 page

Colors

Designer to choose colors to be used in the design.

Requirements
Must have
• Simple and clean. Individual assets must be provided in the correct size and format(png or jpeg). Prefer Goggle fonts. Even though the logo color is red, grey and black, still prefer some modern colors that go well with red. When design, must consider the possibility to convert it into responsive.
Nice to have
• White background
Should not have
• real life photos, no slider

```html
<!DOCTYPE html>
<html lang="en">
<head>
<meta charset="utf-8">
<title>Quorvanta.net – Quality Web Solution</title>
<link rel="stylesheet" href="https://fonts.googleapis.com/css2?family=Poppins:ital,wght@0,500;0,700;0,800;1,400&family=PT+Sans:ital,wght@0,400;0,700;1,400&display=swap">
<style>
:root{
  --red:#f5120f;
  --orange:#ff6a16;
  --grad:linear-gradient(90deg,#ff1b1b 0%,#ff6a1a 100%);
  --dark:#2f2f33;
  --text:#222;
  --maroon:#7a0707;
  --grey-panel:#ececec;
  --footer:#5e5c5c;
  --white:#fff;
  --blush:#f8dfe1;
}
*{margin:0;padding:0;box-sizing:border-box}
html,body{width:1200px;height:3200px;overflow:hidden;background:var(--white)}
body{position:relative;font-family:"PT Sans",sans-serif;color:var(--text)}
.abs{position:absolute}
h1,h2,h3{font-family:"Poppins",sans-serif}

/* header */
.brand{left:56px;top:22px}
.brand-name{font-family:"PT Sans",sans-serif;font-size:38px;font-weight:400;color:#333;letter-spacing:-1px;line-height:1}
.hero-shape{left:0;top:0}
.phone{right:47px;top:12px;color:#fff;font-size:15px;display:flex;align-items:center;gap:6px}
.nav{top:46px;right:47px;display:flex;gap:24px}
.nav a{color:#fff;text-decoration:none;font-weight:700;font-size:15px}
.hero-art{left:106px;top:106px;width:447px;height:341px;border-radius:48% 52% 30% 40%;background:linear-gradient(135deg,#efefef,#d9d9de 60%,#44425a)}
.hero-title{left:722px;top:125px;color:#fff;font-weight:800;font-size:56px;line-height:64px}
.hero-sub{left:724px;top:263px;color:#fff;font-family:"Poppins",sans-serif;font-size:20px}
.email{left:722px;top:329px;width:375px;height:49px;border-radius:25px;background:#fff;box-shadow:0 4px 10px rgba(0,0,0,.15);padding-left:32px;display:flex;align-items:center;font-family:"Poppins",sans-serif;font-style:italic;font-size:19px;color:#888}
.btn-start{left:847px;top:400px;width:131px;height:32px;border-radius:16px;background:var(--maroon);color:#fff;font-family:"Poppins",sans-serif;font-weight:700;font-size:13px;display:flex;align-items:center;justify-content:center;box-shadow:0 3px 8px rgba(0,0,0,.25)}

/* sections */
.sec-title{font-weight:800;color:var(--dark);font-size:46px;line-height:1}
.sec-bar{height:6px;width:40px;border-radius:3px;background:var(--red)}
.copy{font-size:14px;line-height:20px;text-align:justify}
.art{border-radius:40% 50% 45% 35%}
.btn-pill{border-radius:14px;background:var(--red);color:#fff;font-size:13px;display:flex;align-items:center;justify-content:center}

/* news */
.news{left:0;top:1328px;width:1200px;height:436px;background:var(--grad)}
.news-title{left:0;width:1200px;top:1371px;text-align:center;color:#fff;font-size:48px;font-weight:800}
.card{top:1469px;width:258px;height:174px;background:#fff;border-radius:6px;box-shadow:0 6px 14px rgba(0,0,0,.18);overflow:hidden}
.card h3{position:absolute;left:23px;top:24px;font-size:23px;line-height:24px;font-weight:700;color:var(--dark)}
.card p{position:absolute;left:23px;font-size:13px;line-height:16px;color:#333;width:190px}
.card-foot{position:absolute;left:0;bottom:0;width:100%;height:40px;background:#efefef;display:flex;align-items:center;justify-content:space-between;padding:0 18px 0 23px}
.card-foot time{font-family:"Poppins",sans-serif;font-style:italic;font-size:10px;color:#444}
.card-foot .btn-pill{width:88px;height:26px;font-family:"Poppins",sans-serif;font-size:11px;font-weight:500}
.news-more{top:1684px;left:0;width:1200px;text-align:center;color:#fff;font-family:"Poppins",sans-serif;font-weight:700;font-size:18px}

/* company */
.company-copy{left:168px;top:1921px;width:884px;font-size:13.5px;line-height:16px;color:#222}
.company-copy p{margin-bottom:16px}

/* faq */
.faq{left:0;top:2207px;width:1200px;height:391px;background:var(--grad)}
.faq-title{left:0;width:1200px;top:2250px;display:flex;justify-content:center;align-items:center;gap:14px;color:#fff;font-size:36px;font-weight:800}
.faq-rule{left:209px;width:781px;height:1px;background:rgba(255,255,255,.85)}
.faq-q{left:209px;width:781px;height:44px;display:flex;align-items:center;color:#fff;font-weight:700;font-size:15px}
.faq-q .mark{width:55px;text-align:center;font-family:"Poppins",sans-serif;font-size:24px;font-weight:700}
.faq-q .chev{margin-left:auto;margin-right:6px}
.faq-a{left:264px;top:2400px;width:670px;color:#fff;font-size:14px;line-height:16px}

/* philosophy + contact */
.philo{left:0;top:2598px;width:596px;height:434px;background:var(--grey-panel)}
.philo-title{left:106px;top:2720px;font-size:35px;font-weight:700;color:var(--dark)}
.philo-copy{left:106px;top:2786px;width:350px;font-size:11.5px;line-height:20px;color:#333}
.contact-title{left:760px;top:2650px;display:flex;align-items:center;gap:30px;color:var(--red);font-size:36px;font-weight:800}
.field{left:746px;width:296px;border-bottom:1px solid var(--red);font-family:"Poppins",sans-serif;font-style:italic;font-size:14px;color:#888;padding-left:16px;padding-bottom:4px}
.btn-send{left:812px;top:2953px;width:165px;height:38px;border-radius:19px;background:var(--grad);color:#fff;font-family:"Poppins",sans-serif;font-weight:700;font-size:17px;display:flex;align-items:center;justify-content:center}

/* footer */
.footer{left:0;top:3032px;width:1200px;height:168px;background:var(--footer)}
.foot-head{font-family:"Poppins",sans-serif;font-weight:700;color:#fff;font-size:17px}
.affil-head{left:72px;top:3060px;color:#c9c9c9;font-size:27px}
.affil-name{left:72px;top:3112px;width:164px;height:47px;display:flex;align-items:center;gap:8px;color:#fff;font-size:15px;font-weight:700}
.affil-name i{width:12px;height:12px;background:#fff;display:block}
.foot-list{font-size:11px;line-height:20px;color:#fff}
.foot-list span{display:inline-block;width:74px}
.social{left:1047px;top:3110px;display:flex;gap:17px}
.social i{width:20px;height:20px;border-radius:3px;background:#fff;display:block}
.copyright{left:0;width:1200px;top:3174px;text-align:center;font-size:10px;color:#ddd;word-spacing:2px}
.copyright span{margin:0 10px}
</style>
</head>
<body>

<svg class="abs hero-shape" width="1200" height="540" viewBox="0 0 1200 540" aria-hidden="true">
  <defs>
    <linearGradient id="heroGrad" x1="0" y1="0" x2="0.3" y2="1">
      <stop offset="0" stop-color="#f51a0a"/>
      <stop offset="1" stop-color="#ff6a12"/>
    </linearGradient>
  </defs>
  <path d="M584 0 L1200 0 L1200 450 L690 500 Q640 505 640 470 Z" fill="#d2d2d2"/>
  <path d="M584 0 L1200 0 L1200 472 L740 528 Q670 536 660 470 Z" fill="url(#heroGrad)"/>
</svg>

<header>
  <div class="abs brand">
    <div class="brand-name">quorvanta.net</div>
  </div>
  <div class="abs phone">
    <svg width="15" height="15" viewBox="0 0 24 24" aria-hidden="true"><path fill="#fff" d="M6.6 10.8a15.1 15.1 0 0 0 6.6 6.6l2.2-2.2c.3-.3.7-.4 1-.2 1.1.4 2.3.6 3.6.6.6 0 1 .4 1 1V20c0 .6-.4 1-1 1A17 17 0 0 1 3 4c0-.6.4-1 1-1h3.5c.6 0 1 .4 1 1 0 1.3.2 2.5.6 3.6.1.3 0 .7-.2 1z"/></svg>
    +61 7 5550 0142
  </div>
  <nav class="abs nav">
    <a href="#">Home</a><a href="#">Our Services</a><a href="#">Our Clients</a><a href="#">Contact</a>
  </nav>
</header>

<section>
  <div class="abs hero-art" role="img" aria-label="Illustration of a person walking past a large code screen with a small tree"></div>
  <h1 class="abs hero-title">QUALITY WEB<br>SOLUTION</h1>
  <div class="abs hero-sub">AT COMPETITIVE PRICES</div>
  <div class="abs email">Enter email</div>
  <div class="abs btn-start">GET STARTED</div>
</section>

<section>
  <h2 class="abs sec-title" style="left:170px;top:644px">ABOUT US</h2>
  <div class="abs sec-bar" style="left:180px;top:697px"></div>
  <p class="abs copy" style="left:199px;top:724px;width:358px">We have provided web design, graphic design and application development solutions for a wide variety of industries. We are known for the quality of our work, affordable rates and our individual approach to each customer. Our company offers a wide variety of professional web solution and all this at very competitive prices!</p>
  <div class="abs art" style="left:640px;top:627px;width:341px;height:224px;background:linear-gradient(135deg,var(--blush),#f3c9cc)" role="img" aria-label="Illustration of two people working together at a desk computer beside a potted plant"></div>
</section>

<section>
  <div class="abs art" style="left:211px;top:987px;width:329px;height:255px;background:linear-gradient(135deg,#fbe7e8,#eec3c7)" role="img" aria-label="Illustration of two business people shaking hands in an office lobby"></div>
  <h2 class="abs sec-title" style="left:637px;top:987px">OUR CLIENTS</h2>
  <div class="abs sec-bar" style="left:648px;top:1041px"></div>
  <p class="abs copy" style="left:671px;top:1068px;width:358px">We undertake many projects from small businesses to large corporations. We are also extremely experienced in the long term support of comprehensive web based business systems providing first class development, maintenance, data entry services and enhancements.</p>
  <div class="abs btn-pill" style="left:671px;top:1186px;width:92px;height:26px">Read More</div>
</section>

<section>
  <div class="abs news"></div>
  <h2 class="abs news-title">NEWS</h2>

  <article class="abs card" style="left:163px">
    <h3>WEBSITE :</h3>
    <p style="top:60px">Quorvanta.net launches new website.</p>
    <div class="card-foot"><time>May 10, 2019</time><div class="btn-pill">Read More&nbsp;&rsaquo;</div></div>
  </article>
  <article class="abs card" style="left:470px">
    <h3>Lorem ipsum<br>dolor sit</h3>
    <p style="top:82px">Lorem ipsum dolor sit amet, consectetur adipiscing elit, sed.</p>
    <div class="card-foot"><time>May 10, 2019</time><div class="btn-pill">Read More&nbsp;&rsaquo;</div></div>
  </article>
  <article class="abs card" style="left:776px">
    <h3>WEBSITE :</h3>
    <p style="top:60px">Quorvanta.net launches new website.</p>
    <div class="card-foot"><time>May 10, 2019</time><div class="btn-pill">Read More&nbsp;&rsaquo;</div></div>
  </article>

  <div class="abs news-more">More &rsaquo;</div>
</section>

<section>
  <h2 class="abs sec-title" style="left:106px;top:1830px">OUR COMPANY</h2>
  <div class="abs sec-bar" style="left:114px;top:1881px"></div>
  <div class="abs company-copy">
    <p>Quorvanta.net is an Australian based Software and Web Development Company that provides individual technology solutions and professional software for clients worldwide.</p>
    <p>Our work is based on quality sales, customer and technical support services.</p>
    <p>Being oriented towards innovative productivity in our work, we come up with essential tools for online business enhancing. Our programming specialists focus on delivering solutions for small start-ups as well as large organizations and companies. The team of purposeful and experienced professionals works hard to extract maximum performance from modern information technologies.</p>
    <p>Providing the best quality of service and excellence of support we established a global presence in the software market. Our clients come from all over the world.</p>
    <p>Click here for more information on the services we provide.</p>
  </div>
</section>

<section>
  <div class="abs faq"></div>
  <h2 class="abs faq-title">
    <svg width="36" height="32" viewBox="0 0 36 32" aria-hidden="true">
      <rect x="12" y="0" width="22" height="17" rx="2" fill="#fff"/>
      <path d="M26 17 L30 22 L30 17 Z" fill="#fff"/>
      <rect x="2" y="10" width="20" height="16" rx="2" fill="#fff" stroke="#ff3a18" stroke-width="2"/>
      <path d="M6 26 L4 31 L11 26 Z" fill="#fff"/>
    </svg>
    FAQ
  </h2>
  <div class="abs faq-rule" style="top:2330px"></div>
  <div class="abs faq-q" style="top:2331px"><span class="mark">?</span>How much does a website powered by Quorvanta.net cost?
    <svg class="chev" width="14" height="9" viewBox="0 0 14 9" aria-hidden="true"><path d="M1 8 L7 2 L13 8" stroke="#fff" stroke-width="2" fill="none"/></svg></div>
  <div class="abs faq-rule" style="top:2376px"></div>
  <p class="abs faq-a">There are quite a few factors that are going to affect the ultimate cost of your web site. These factors include how many pages you are going to have, if you will sell products on your website, the graphic work involved, and how interactive your web site will be.</p>
  <div class="abs faq-rule" style="top:2475px"></div>
  <div class="abs faq-q" style="top:2476px"><span class="mark">?</span>How long does it take to have a website designed?
    <svg class="chev" width="14" height="9" viewBox="0 0 14 9" aria-hidden="true"><path d="M1 1 L7 7 L13 1" stroke="#fff" stroke-width="2" fill="none"/></svg></div>
  <div class="abs faq-rule" style="top:2520px"></div>
</section>

<section>
  <div class="abs philo"></div>
  <h2 class="abs philo-title">PHILOSOPHY</h2>
  <p class="abs philo-copy">As web developers, we understand that a powerful and functional web site is a vital component of modern day marketing for companies of today. This is why our web site development team work with all of our clients to ensure their web site design will deliver to their target market.</p>

  <h2 class="abs contact-title">
    <svg width="26" height="24" viewBox="0 0 26 24" aria-hidden="true"><path d="M25 1 L1 10 L9 13 L11 22 L15 15 L25 1 Z M9 13 L25 1" fill="#f5120f" stroke="#f5120f" stroke-width="1" stroke-linejoin="round"/></svg>
    CONTACT
  </h2>
  <div class="abs field" style="top:2740px">Name</div>
  <div class="abs field" style="top:2781px">Email</div>
  <div class="abs field" style="top:2880px">Message</div>
  <div class="abs btn-send">SEND</div>
</section>

<footer>
  <div class="abs footer"></div>
  <div class="abs foot-head affil-head">AFFILIATES</div>
  <div class="abs affil-name"><i></i>Lumenfold Studio</div>

  <div class="abs foot-head" style="left:376px;top:3060px">CALL US TODAY</div>
  <div class="abs foot-list" style="left:378px;top:3100px">
    <div><span>Phone</span>+61 7 5550 0142</div>
    <div><span>Mobile</span>+61 0400 555 019</div>
  </div>

  <div class="abs foot-head" style="left:641px;top:3060px">WRITE US</div>
  <div class="abs foot-list" style="left:643px;top:3100px">
    <div><span>Sales</span>info@quorvanta.net</div>
    <div><span>Support</span>support@quorvanta.net</div>
  </div>

  <div class="abs social" aria-label="Social links"><i></i><i></i><i></i></div>

  <div class="abs copyright"><span>Copyright 2019</span><span>Quorvanta.net</span></div>
</footer>

</body>
</html>
```